International Life Insurer Needs a Web Design

What We Do: We are a boutique financial services firm specializing in solutions that financial services professionals can integrate into comprehensive wealth preservation strategies for their clients. Strategies we provide may run the spectrum from simple life insurance products to complex cases with very sophisticated and intricate solutions.

Industry Type: Financial & Insurance

Top Things to Communicate Through Our Web Design:
#1 Ultra High Net Worth
#2 INTERNATIONAL
#3 Private Banking
#4 Expertise
________________________________________
Our Target Audience:
Financial institutions/private banks who have high net worth/ultra high net worth international clients looking for unparalleled expertise in wealth preservation, taxation, and business insurance. The audience is the financial service professional, not the end client of the financial services. We will direct the professional to the site.
We Like These Designs. (fonts, colors, style):
Simple font, clean, modern, contemporary, blue colors
NOT stodgy, old, gothic, etc.

Secondarily, we’d like to also create a small tri-fold brochure incorporating the web elements (design, text), so the ability to transfer the design to print might be a plus.
Updates

Target Market(s)

Financial services professionals catering to their ultra high net worth clients

Industry/Entity Type

Life Insurance

Requirements
Must have
• Our logo (see uploaded file)
Nice to have
• the existing website includes some text that could be reviewed for ideas and incorporated into the design: http://harborlinecoveragepartners.example/

```html
<!DOCTYPE html>
<html lang="en">
<head>
<meta charset="utf-8">
<title>Harborline Coverage Partners</title>
<link rel="stylesheet" href="https://fonts.googleapis.com/css2?family=PT+Sans+Narrow&family=Source+Sans+3:wght@400;600&display=swap">
<style>
:root{
  --navy:#0b2f6b;
  --footer:#1c4a80;
  --footer-dark:#0b1f3d;
  --accent:#1a8fd6;
  --link:#2a8bc0;
  --ink:#3b3b3b;
  --muted:#5d5d5d;
  --page:#ececec;
  --panel:#ffffff;
  --field:#f1f1f1;
  --band:#d6d6d6;
}
*{box-sizing:border-box;margin:0;padding:0}
html,body{width:1200px;height:1200px;overflow:hidden;background:var(--page)}
.stage{position:relative;width:1400px;height:1400px;transform:scale(.857143);transform-origin:0 0;background:var(--page);font-family:"Source Sans 3",sans-serif;color:var(--muted)}
.abs{position:absolute}
.topbar{left:0;top:0;width:1400px;height:8px;background:var(--navy)}
.brand{left:210px;top:25px;display:flex;align-items:center;gap:10px}
.brand-mark{width:73px;height:73px;background:var(--navy)}
.brand-name{font-size:30px;line-height:28px;color:var(--navy);font-weight:400;letter-spacing:-.5px}
.nav{left:689px;top:53px;display:flex;font-family:"PT Sans Narrow",sans-serif;font-size:17px;letter-spacing:2px;color:#333}
.nav span{margin-right:42px}
.nav span:last-child{margin-right:0}
.nav .active{color:var(--accent)}
.hero{left:213px;top:119px;width:960px;height:381px;border-top:6px solid #a9c6e4;background:linear-gradient(180deg,#5f86b4 0%,#a9bfd6 35%,#4d6f94 62%,#8fb0cf 78%,#3f6690 100%)}
.heading-row{display:flex;align-items:center;gap:12px}
.heading{font-family:"PT Sans Narrow",sans-serif;font-size:21px;letter-spacing:1.6px;color:#3a3a3a;white-space:nowrap;flex:none}
.heading em{font-style:normal;color:var(--accent)}
.band{height:14px;background:var(--band);flex:1}
.tab{width:0;height:0;border-left:17px solid transparent;border-bottom:26px solid var(--panel)}
.panel{background:var(--panel)}
.body{font-size:13px;line-height:24px;color:var(--muted)}
.dot{display:inline-block;width:9px;height:9px;border-radius:50%;background:var(--link);margin-right:6px;vertical-align:0}
.btn{display:inline-block;background:var(--navy);color:#fff;font-size:12px;font-weight:600;padding:0 23px;height:30px;line-height:30px}
.card-img{width:230px;height:117px}
.card-title{font-size:14px;font-weight:600;color:#333;margin:11px 10px 9px}
.card-text{font-size:12.5px;line-height:20px;color:var(--muted);padding:0 12px}
.more{color:var(--link)}
.sub{font-size:14px;font-weight:600;color:#333}
.divider{left:529px;top:910px;height:232px;border-left:1px dotted #aaa}
.label{font-size:12.5px;color:var(--link)}
.field{width:249px;height:29px;background:var(--field);border:1px solid #c9c9c9;font-size:11.5px;font-style:italic;color:#444;padding-left:12px;line-height:27px;letter-spacing:.3px}
.go{width:28px;height:27px;background:var(--navy);color:#fff;font-size:11px;font-weight:600;text-align:center;line-height:26px}
.footer{left:0;top:1254px;width:1400px;height:134px;background:var(--footer)}
.footer-base{left:0;top:1388px;width:1400px;height:12px;background:var(--footer-dark)}
.foot-text{font-size:11.5px;line-height:24px;color:#fff}
.foot-links{font-size:12px;line-height:24px;color:#fff;text-align:right}
.foot-links .current{color:var(--accent)}
</style>
</head>
<body>
<div class="stage">
  <div class="abs topbar"></div>

  <header>
    <div class="abs brand">
      <div class="brand-mark"></div>
      <div class="brand-name">Harborline Coverage<br>Partners</div>
    </div>
    <nav class="abs nav">
      <span class="active">HOME</span><span>ABOUT</span><span>SOLUTIONS</span><span>CASE SUDIES</span><span>CONTACT</span>
    </nav>
  </header>

  <div class="abs hero" role="img" aria-label="City skyline at dusk reflected in calm harbour water"></div>

  <div class="abs heading-row" style="left:230px;top:521px;width:943px">
    <div class="heading">SPECIALIZING IN COMPREHENSIVE <em>WEALTH PRESERVATION STRATEGIES FOR OUR CLIENTS</em></div>
    <div class="band"></div>
  </div>
  <div class="abs tab" style="left:213px;top:540px"></div>

  <section class="abs panel" style="left:213px;top:566px;width:472px;height:245px;padding:14px 18px 0 21px">
    <p class="body"><span class="dot"></span>SIn posuere ante in orci molestie adipiscing porta quam commodo. Suspendisse ut ligula nisi, cursus ullamcorper orci.</p>
    <p class="body">Nulla vulputate sodales metus, eget dignissim mi volutpat eu. Pellentesque nisi sem, euismod sit amet bibendum at, euismod a est. Morbi mattis bibendum sapien at ullamcorper.</p>
    <p class="body">Proin hendrerit, justo id hendrerit consectetur, lectus elit rhoncus eros, et adipiscing felis quam at nibh. Maecenas tincidunt pretium lectus, at tempor arcu</p>
    <a class="btn" style="margin-top:14px">read more</a>
  </section>

  <article class="abs panel" style="left:698px;top:566px;width:230px;height:245px">
    <div class="card-img" role="img" aria-label="Hands signing a financial document beside charts" style="background:linear-gradient(135deg,#e8ecef 0%,#b9c3cc 60%,#f2f2f2 100%)"></div>
    <h3 class="card-title">Image Headline One</h3>
    <p class="card-text">Cam sociis natoque penatibus et magnis dis parturient montes, nascetur ridiculus mus. Nunc a viverra turpis susepi &nbsp;<span class="more">read more &rarr;</span></p>
  </article>

  <article class="abs panel" style="left:942px;top:566px;width:230px;height:245px">
    <div class="card-img" role="img" aria-label="Business team meeting in a bright office" style="background:linear-gradient(135deg,#dfe6ea 0%,#a7b4bd 55%,#eef1f3 100%)"></div>
    <h3 class="card-title">Image Headline Two</h3>
    <p class="card-text">Cam sociis natoque penatibus et magnis dis parturient montes, nascetur ridiculus mus. Nunc a viverra turpis susepi &nbsp;<span class="more">read more &rarr;</span></p>
  </article>

  <div class="abs heading-row" style="left:231px;top:849px;width:616px">
    <div class="heading">HEADLINE <em>TWO</em></div>
    <div class="band"></div>
  </div>
  <div class="abs tab" style="left:213px;top:867px"></div>
  <div class="abs heading-row" style="left:874px;top:849px;width:297px">
    <div class="heading">FIND OUT <em>MORE</em></div>
    <div class="band"></div>
  </div>

  <section class="abs panel" style="left:213px;top:893px;width:633px;height:266px"></section>
  <div class="abs" style="left:233px;top:916px;width:272px">
    <h3 class="sub">Lower Headline One</h3>
    <p class="body" style="line-height:20px;margin-top:18px"><span class="dot"></span>In posuere ante in orci molestie adipiscing porta quam commodo. Suspendisse ut ligula nisi, cursus ullamcorper orci. Nulla vulputate sodales metus, eget dignissim mi volutpat eu. Pellentesque nisi sem, euismod sit amet bibendum at, euismod a est. Morbi mattis bibendum sapien at ullamcorper. significant returns.</p>
    <p class="more" style="font-size:14px;margin:18px 0 0 7px">read more &rarr;</p>
  </div>
  <div class="abs divider"></div>
  <div class="abs" style="left:553px;top:916px;width:275px">
    <h3 class="sub">Lower Headline Two</h3>
    <p class="body" style="line-height:20px;margin-top:18px"><span class="dot"></span>In posuere ante in orci molestie adipiscing porta quam commodo. Suspendisse ut ligula nisi, cursus ullamcorper orci.<br>Nulla vulputate sodales metus, eget dignissim mi volutpat eu. Pellentesque nisi sem, euismod sit amet bibendum at, euismod a est.<br>Morbi mattis bibendum sapien at ullamcorper.</p>
    <p class="more" style="font-size:14px;margin-top:18px">read more &nbsp;&rarr;</p>
  </div>

  <section class="abs panel" style="left:861px;top:893px;width:312px;height:266px;padding:21px 0 0 13px">
    <p class="sub" style="line-height:22px">If you are interested in our service<br>please fill in our form</p>
    <p class="label" style="margin:7px 0 0 2px">Your Name</p>
    <div class="field" style="margin-top:6px">Enter your full name and title</div>
    <p class="label" style="margin:11px 0 0 2px">Business Name :</p>
    <div class="field" style="margin-top:6px">Please enter name &amp; City branch</div>
    <p class="label" style="margin:9px 0 0 2px">Your Email :</p>
    <div style="display:flex;align-items:center;gap:8px;margin-top:6px">
      <div class="field">Please enter email address</div>
      <div class="go">go</div>
    </div>
  </section>

  <footer>
    <div class="abs footer"></div>
    <div class="abs foot-text" style="left:211px;top:1270px">&copy; Copyright 2012 &nbsp;All rights reserved.<br><span style="line-height:30px">233 Street Blvd., Second Add.</span><br>City Name, &nbsp;123456<br>Tel: 0000 1234567</div>
    <div class="abs foot-links" style="left:935px;top:1270px;width:100px"><span class="current">Homepage</span><br>About Us<br>Solutions<br>Contact Us</div>
    <div class="abs foot-links" style="left:1067px;top:1272px;width:100px">Case Studies<br>Disclaimer<br>Privacy Policy<br>Social Media</div>
    <div class="abs footer-base"></div>
  </footer>
</div>
</body>
</html>
```